Four Oaks Haulage Website (quoting web application)

We need a website designed for our furniture moving company in Cape Town, South Africa.

I have attached some logos and images for you to use.

I have also attached the layout of the three pages we want designed (pdf file)

Dark blue is our colour.

The pictures of our trucks (uploaded) epitomise the design required.

Our old site (existing) is viewable here: fouroakshaulage.co.za

Target Market(s)

People moving house in Cape Town, South Africa.

Number of Pages Required

3 page

Font styles to use
Sans Serif

Colors
0255a3

Requirements
Must have
• Page design for the 3 pages in the pdf file.

```html
<!DOCTYPE html>
<html lang="en">
<head>
<meta charset="utf-8">
<title>Four Oaks Haulage – Cape Town Furniture Movers</title>
<link href="https://fonts.googleapis.com/css2?family=Montserrat:wght@400;500;600;700&family=Open+Sans:wght@400;600&family=Dancing+Script:wght@500&display=swap" rel="stylesheet">
<style>
:root{
  --brand:#0255a3;
  --brand-dark:#0a3f7a;
  --ink:#2d3440;
  --text:#6b717a;
  --muted:#9aa0a8;
  --line:#e6e8eb;
  --pale:#f4f6f9;
  --bar:#4a4f57;
  --footer:#3f444c;
  --gold:#f5b400;
  --pink:#e0457b;
  --white:#ffffff;
}
*{box-sizing:border-box;margin:0;padding:0}
html,body{width:1200px;height:3390px;overflow:hidden}
body{position:relative;background:var(--white);font-family:"Open Sans",Arial,sans-serif;color:var(--text)}
.abs{position:absolute}
.heading{font-family:"Montserrat",Arial,sans-serif}

/* header */
.site-header{left:0;top:0;width:1200px;height:158px;background:var(--white)}
.brand-name{left:112px;top:58px;font-family:"Montserrat",Arial,sans-serif;font-weight:700;font-size:25px;color:var(--brand-dark);display:flex;align-items:center;gap:12px;line-height:1.05}
.brand-name .dot{width:34px;height:34px;background:var(--brand-dark);border-radius:50%}
.help{right:110px;top:30px;font-size:16px;color:var(--ink);text-align:right}
.contact-line{right:110px;top:56px;font-size:16px;color:var(--muted)}
.contact-line b{font-weight:400;color:var(--brand)}
.nav{left:432px;top:110px;display:flex;gap:32px;font-family:"Montserrat",Arial,sans-serif;font-size:11.5px;font-weight:600;color:var(--ink);letter-spacing:.3px}
.nav .active{color:var(--brand);position:relative}
.nav .active::after{content:"";position:absolute;left:-20px;right:-20px;top:45px;height:3px;background:var(--brand)}
.btn-quote{left:940px;top:102px;width:150px;height:34px;background:var(--brand-dark);color:var(--white);font-family:"Montserrat",Arial,sans-serif;font-size:11px;font-weight:600;display:flex;align-items:center;justify-content:center}

/* hero */
.hero-photo{left:0;top:158px;width:1200px;height:442px;background:linear-gradient(100deg,#8c8f93 0%,#5d6670 30%,#1e3f7a 62%,#15306a 100%)}
.hero-title{left:0;top:326px;width:1200px;text-align:center;color:var(--white);font-family:"Montserrat",Arial,sans-serif;font-weight:600;font-size:36px}
.hero-sub{left:0;top:370px;width:1200px;text-align:center;color:var(--white);font-size:16px}
.hero-btn{left:530px;top:418px;width:140px;height:40px;border:1px solid var(--white);color:var(--white);font-family:"Montserrat",Arial,sans-serif;font-size:11px;font-weight:600;display:flex;align-items:center;justify-content:center}
.hero-dots{left:1010px;top:552px;display:flex;gap:8px}
.hero-dots span{width:30px;height:30px;border-radius:50%;background:rgba(255,255,255,.3)}
.info-bar{left:0;top:600px;width:1200px;height:68px;background:var(--bar)}
.info-bar p{position:absolute;left:110px;top:24px;color:#d6d9dd;font-size:14.5px}
.info-bar b{color:var(--white);font-weight:600}
.info-bar .btn{position:absolute;left:940px;top:15px;width:150px;height:38px;border:1px solid var(--white);color:var(--white);font-family:"Montserrat",Arial,sans-serif;font-size:11px;font-weight:600;display:flex;align-items:center;justify-content:center}

/* about */
.about-strip{left:0;top:760px;width:85px;height:440px;background:var(--pale)}
.about-tag{left:195px;top:782px;font-family:"Montserrat",Arial,sans-serif;font-size:12px;font-weight:600;letter-spacing:1.5px;color:var(--ink)}
.about-title{left:195px;top:826px;width:380px;font-family:"Montserrat",Arial,sans-serif;font-size:28px;font-weight:600;color:var(--brand);line-height:1.25}
.about-copy{left:195px;top:912px;width:440px;font-size:14px;line-height:1.7}
.about-copy p+p{margin-top:12px}
.about-btn{left:195px;top:1128px;width:140px;height:36px;border:2px solid var(--brand);color:var(--brand);font-family:"Montserrat",Arial,sans-serif;font-size:11px;font-weight:600;display:flex;align-items:center;justify-content:center}
.about-photo{left:698px;top:760px;width:502px;height:440px;background:linear-gradient(135deg,#87b8e0 0%,#3aa9c9 35%,#1f2226 60%,#8a8f94 100%)}

/* features */
.feature{top:1290px;width:250px;text-align:center}
.feature svg{display:block;margin:0 auto 14px}
.feature h3{font-family:"Montserrat",Arial,sans-serif;font-size:15px;font-weight:600;color:var(--ink);margin-bottom:8px}
.feature p{font-size:12px;line-height:1.6;color:var(--text);padding:0 20px}
.arrow{font-family:"Montserrat",Arial,sans-serif;font-size:22px;color:var(--ink)}
.arrow.blue{color:var(--brand)}

/* services */
.tile{background:linear-gradient(160deg,#8a8679,#5b5248)}
.tile-label{display:flex;align-items:center;justify-content:center;text-align:center;color:var(--white);font-family:"Montserrat",Arial,sans-serif;font-weight:600;font-size:15px;line-height:1.3;letter-spacing:.5px;text-transform:uppercase}
.service-panel{left:480px;top:1520px;width:240px;height:515px}
.service-panel h2{position:absolute;left:0;top:46px;width:240px;text-align:center;color:var(--white);font-family:"Montserrat",Arial,sans-serif;font-size:24px;font-weight:600;line-height:1.3}
.service-panel p{position:absolute;left:30px;top:150px;width:180px;text-align:center;color:var(--white);font-size:13px;line-height:1.6}
.service-panel .btn{position:absolute;left:48px;top:375px;width:144px;height:50px;border:1px solid var(--white);color:var(--white);font-family:"Montserrat",Arial,sans-serif;font-size:10.5px;font-weight:600;text-align:center;display:flex;align-items:center;justify-content:center;line-height:1.4}

/* testimonials */
.love-title{left:0;top:2108px;width:1200px;text-align:center;font-family:"Montserrat",Arial,sans-serif;font-size:27px;font-weight:600;color:var(--brand)}
.love-script{left:0;top:2138px;width:1200px;text-align:center;font-family:"Dancing Script",cursive;font-size:34px;color:var(--pink)}
.card{top:2225px;width:300px;height:395px;border:1px solid var(--line);background:var(--white);text-align:center}
.card.raised{top:2222px;box-shadow:0 14px 34px rgba(20,40,80,.14);border-color:transparent}
.card .source{margin-top:28px;font-family:"Montserrat",Arial,sans-serif;font-size:20px;font-weight:600;color:var(--brand)}
.card .stars{margin-top:18px;color:var(--gold);font-size:18px;letter-spacing:3px}
.card .quote{margin:14px auto 0;width:230px;font-size:13px;line-height:1.65;color:var(--text)}
.card .avatar{width:60px;height:60px;border-radius:50%;margin:28px auto 10px;background:linear-gradient(135deg,#b9a58f,#5a4a3e)}
.card .name{font-family:"Montserrat",Arial,sans-serif;font-size:13px;font-weight:600;color:var(--ink)}
.card .when{font-size:11px;color:var(--muted);margin-top:4px}

/* CTA */
.cta{left:0;top:2710px;width:1200px;height:260px;background:var(--brand)}
.cta h2{position:absolute;left:0;top:56px;width:1200px;text-align:center;color:var(--white);font-family:"Montserrat",Arial,sans-serif;font-size:31px;font-weight:600}
.cta p{position:absolute;left:0;top:104px;width:1200px;text-align:center;color:var(--white);font-size:20px}
.cta .btn{position:absolute;top:146px;width:198px;height:44px;font-family:"Montserrat",Arial,sans-serif;font-size:11px;font-weight:600;display:flex;align-items:center;justify-content:center}
.cta .solid{left:395px;background:var(--white);color:var(--brand)}
.cta .ghost{left:605px;border:1px solid var(--white);color:var(--white)}

/* footer */
.site-footer{left:0;top:2970px;width:1200px;height:420px;background:var(--footer);text-align:center;color:#d9dce0}
.footer-brand{position:absolute;left:0;top:92px;width:1200px;font-family:"Montserrat",Arial,sans-serif;font-weight:700;font-size:24px;color:var(--white)}
.footer-contact{position:absolute;left:0;top:160px;width:1200px;font-size:16px}
.footer-links{position:absolute;left:0;top:192px;width:1200px;font-family:"Montserrat",Arial,sans-serif;font-size:11px;font-weight:600;display:flex;justify-content:center;gap:22px;color:#cfd3d8}
.footer-links .current{color:var(--white)}
.footer-social{position:absolute;left:0;top:244px;width:1200px;display:flex;justify-content:center;gap:22px}
.footer-social span{width:22px;height:22px;border-radius:50%;background:#b9bec5}
.footer-copy{position:absolute;left:0;top:294px;width:1200px;font-size:13px;line-height:1.8;color:#c6cad0}
</style>
</head>
<body>

<header class="abs site-header">
  <div class="abs brand-name"><span class="dot"></span><span>FOUR OAKS<br>HAULAGE</span></div>
  <div class="abs help">Need Help? Contact Us Today!</div>
  <div class="abs contact-line">Call: <b>021 555 0187</b> &nbsp;|&nbsp; E. <b>bookings@fouroaks.co.za</b></div>
  <nav class="abs nav">
    <span class="active">HOME</span><span>ABOUT</span><span>OUR SERVICES</span><span>WHY CHOOSE US?</span><span>CONTACT</span>
  </nav>
  <div class="abs btn-quote">INSTANT QUOTE</div>
</header>

<section>
  <div class="abs hero-photo" role="img" aria-label="Moving crew in blue overalls standing in front of a blue removal truck"></div>
  <h1 class="abs hero-title">Four Oaks Haulage</h1>
  <p class="abs hero-sub">Trusted Cape Town Mover</p>
  <div class="abs hero-btn">INSTANT QUOTE</div>
  <div class="abs hero-dots"><span></span><span></span></div>
  <div class="abs info-bar">
    <p>We are <b>experienced, trained removal experts</b> who know how to deal with all of your moving situations.</p>
    <div class="btn">CONTACT NOW!</div>
  </div>
</section>

<section>
  <div class="abs about-strip"></div>
  <div class="abs about-tag">PUNCTUALITY. HONESTY. CARE.</div>
  <h2 class="abs about-title">Dedicated Cape Town experts</h2>
  <div class="abs about-copy">
    <p>We are a Cape Town furniture removal company with offices in Woodstock who do furniture removals for Cape Town.</p>
    <p>We have been Cape Town movers since 2012 so if you need furniture removal done well in Cape Town we are your team. We have large trucks for big removals but we also have smaller fuel efficient vehicles which make your mini moves quick and affordable.</p>
  </div>
  <div class="abs about-btn">ABOUT US</div>
  <div class="abs about-photo" role="img" aria-label="Black removal truck parked on a colourful Cape Town street"></div>
</section>

<section>
  <div class="abs arrow" style="left:50px;top:1348px">‹</div>
  <div class="abs arrow blue" style="left:1138px;top:1348px">›</div>
  <div class="abs feature" style="left:95px">
    <svg width="40" height="40" viewBox="0 0 40 40" fill="none" stroke="#9aa0a8" stroke-width="2"><rect x="5" y="18" width="7" height="16"/><path d="M12 20l7-12c3 0 4 2 3 6l-1 4h10c2 0 3 2 2 4l-3 10c-1 2-2 2-4 2H12"/></svg>
    <h3>Fully Insured</h3><p>We will fix or replace any furniture damaged during furniture removal.</p>
  </div>
  <div class="abs feature" style="left:350px">
    <svg width="40" height="40" viewBox="0 0 40 40" fill="none" stroke="#0255a3" stroke-width="2"><path d="M20 3l5 11 12 1-9 8 3 12-11-6-11 6 3-12-9-8 12-1z"/></svg>
    <h3>Special Services</h3><p>We have a range of special services to make your move go smoothly.</p>
  </div>
  <div class="abs feature" style="left:600px">
    <svg width="40" height="40" viewBox="0 0 40 40" fill="none" stroke="#9aa0a8" stroke-width="2"><circle cx="20" cy="13" r="7"/><path d="M7 37c0-8 6-13 13-13s13 5 13 13"/></svg>
    <h3>Trained Experts</h3><p>We have been doing your moves in Cape Town for more than 4 years.</p>
  </div>
  <div class="abs feature" style="left:850px">
    <svg width="40" height="40" viewBox="0 0 40 40" fill="none" stroke="#9aa0a8" stroke-width="2"><circle cx="20" cy="20" r="16"/><circle cx="14" cy="16" r="1.5" fill="#9aa0a8"/><circle cx="26" cy="16" r="1.5" fill="#9aa0a8"/><path d="M12 24c4 5 12 5 16 0"/></svg>
    <h3>Happy Customers</h3><p>Read what our happy customers say about our Cape Town removals.</p>
  </div>
</section>

<section>
  <div class="abs tile" style="left:0;top:1520px;width:240px;height:480px" role="img" aria-label="Mover wheeling a wooden cabinet on a hand truck"></div>
  <div class="abs tile-label" style="left:0;top:1900px;width:240px;height:60px">Hoists &amp; Lifting<br>Furniture</div>
  <div class="abs tile" style="left:240px;top:1520px;width:240px;height:240px;background:linear-gradient(160deg,#6d6a68,#3e3b3a)" role="img" aria-label="Cardboard boxes being packed"></div>
  <div class="abs tile-label" style="left:240px;top:1610px;width:240px;height:60px">Box<br>Packing</div>
  <div class="abs tile" style="left:240px;top:1760px;width:240px;height:240px;background:linear-gradient(160deg,#a8a8aa,#6e6d70)" role="img" aria-label="Items wrapped in bubble wrap"></div>
  <div class="abs tile-label" style="left:240px;top:1900px;width:240px;height:60px">Bubble<br>Wrapping</div>
  <svg class="abs service-panel" viewBox="0 0 240 515" width="240" height="515" aria-hidden="true"><polygon points="0,0 240,0 240,480 120,515 0,480" fill="#0255a3"/></svg>
  <div class="abs service-panel">
    <h2>Furniture<br>Moving Services</h2>
    <p>We are a professional furniture moving company offering home moves, office moves, mini moves and storage.</p>
    <div class="btn">EXPLORE ALL<br>SERVICES</div>
  </div>
  <div class="abs tile" style="left:720px;top:1520px;width:240px;height:480px;background:linear-gradient(160deg,#9c8f7e,#2f3e5a)" role="img" aria-label="Mover in cap and overalls dismantling furniture"></div>
  <div class="abs tile-label" style="left:720px;top:1900px;width:240px;height:60px">Dismantling and<br>Reassembling</div>
  <div class="abs tile" style="left:960px;top:1520px;width:240px;height:240px;background:linear-gradient(160deg,#a9b4bf,#6a6258)" role="img" aria-label="Movers carrying boxes out of a house"></div>
  <div class="abs tile-label" style="left:960px;top:1600px;width:240px;height:60px">Box<br>Delivery</div>
  <div class="abs tile" style="left:960px;top:1760px;width:240px;height:240px;background:linear-gradient(160deg,#c9a77e,#8a6a48)" role="img" aria-label="Stacked cardboard boxes in storage"></div>
  <div class="abs tile-label" style="left:960px;top:1900px;width:240px;height:60px">Short-Term<br>Storage</div>
</section>

<section>
  <h2 class="abs love-title">People of Cape Town</h2>
  <div class="abs love-script">♡ Love Us</div>
  <div class="abs arrow" style="left:50px;top:2405px">‹</div>
  <div class="abs arrow blue" style="left:1138px;top:2405px">›</div>
  <article class="abs card" style="left:110px">
    <div class="source">Chatter</div><div class="stars">★★★★★</div>
    <p class="quote">Thank you to your team and the guys that met me for excellent service, punctuality and willingness. It's a rare find in the service industry today ...</p>
    <div class="avatar" role="img" aria-label="Customer portrait"></div>
    <div class="name">Sam Whitfield</div><div class="when">3 Month Ago</div>
  </article>
  <article class="abs card raised" style="left:445px">
    <div class="source">RateLocal</div><div class="stars">★★★★★</div>
    <p class="quote">Thank you to your team and the guys that met me for excellent service, punctuality and willingness. It's a rare find in the service industry today ...</p>
    <div class="avatar" role="img" aria-label="Customer portrait"></div>
    <div class="name">Lena Marsh</div><div class="when">2 Month Ago</div>
  </article>
  <article class="abs card" style="left:782px">
    <div class="source">Friendbook</div><div class="stars">★★★★★</div>
    <p class="quote">Thank you to your team and the guys that met me for excellent service, punctuality and willingness. It's a rare find in the service industry today ...</p>
    <div class="avatar" role="img" aria-label="Customer portrait"></div>
    <div class="name">Theo Varkas</div><div class="when">1 Month Ago</div>
  </article>
</section>

<section class="abs cta">
  <h2>Get An Instant Quote Today</h2>
  <p>Enter your details, see your quote and book your move now!</p>
  <div class="btn solid">GET AN INSTANT QUOTE</div>
  <div class="btn ghost">TRADITIONAL QUOTE</div>
</section>

<footer class="abs site-footer">
  <div class="footer-brand">FOUR OAKS HAULAGE</div>
  <div class="footer-contact">Call: 021 555 0187 &nbsp;&nbsp;|&nbsp;&nbsp; E. bookings@fouroaks.co.za</div>
  <div class="footer-links"><span class="current">CONTACT</span><span>FAQ</span><span>BLOG</span><span>TERMS &amp; CONDITIONS</span></div>
  <div class="footer-social"><span></span><span></span></div>
  <div class="footer-copy">© 2017 Four Oaks Haulage (Pty) Ltd.<br>Sitemap.</div>
</footer>

</body>
</html>
```